BOLD & MINIMALIST DESIGN NEEDED

We want a very bold but minimalistic business card design that is impactful and utilizes both sides of the business card. Our current logo is included for your use.

We want bold fonts and good use of negative space. We don't want the logo to overpower the design.

Target Market(s)

Professionals who are building new commercial buildings.

Industry/Entity Type

Construction

Contact Information for Business Card

Name, Title, email, office phone, cell phone, website

Font styles to use
Serif
Sans Serif

Requirements
Must have
• Bold design!

```html
<!DOCTYPE html>
<html lang="en">
<head>
<meta charset="utf-8">
<title>Ridgecrest Design + Build — Business Card</title>
<link href="https://fonts.googleapis.com/css2?family=Arimo:wght@400;700&display=swap" rel="stylesheet">
<style>
  :root {
    --backdrop: #dedede;
    --card-white: #f4f4f5;
    --ink: #0b0b0b;
    --text: #1c1c1c;
    --green: #7fba27;
    --green-light: #b4d97a;
    --white: #ffffff;
  }
  * { margin: 0; padding: 0; box-sizing: border-box; }
  html, body {
    width: 1200px;
    height: 1040px;
    overflow: hidden;
    background: var(--backdrop);
    font-family: "Arimo", Arial, sans-serif;
  }
  .canvas { position: relative; width: 1200px; height: 1040px; }

  .card {
    position: absolute;
    border-radius: 16px;
    overflow: hidden;
  }

  /* Front side */
  .card-front {
    left: 286px; top: 130px;
    width: 640px; height: 366px;
    background: var(--card-white);
  }
  .front-brand {
    position: absolute;
    right: 42px; top: 96px;
    display: flex; align-items: center; gap: 10px;
    font-weight: 700; font-size: 22px;
    color: var(--ink);
    letter-spacing: 0.5px;
    text-transform: uppercase;
  }
  .brand-square {
    width: 18px; height: 18px;
    background: var(--green);
  }
  .person-name {
    position: absolute; left: 44px; top: 205px;
    font-weight: 700; font-size: 25px;
    color: var(--ink);
    text-transform: uppercase;
  }
  .person-title {
    position: absolute; left: 44px; top: 232px;
    font-size: 16px; color: var(--green);
  }
  .divider {
    position: absolute; left: 44px; top: 255px;
    width: 554px; height: 1px; background: var(--ink);
  }
  .contact-list {
    position: absolute; left: 44px; top: 268px;
    list-style: none;
    font-size: 16px; color: var(--text);
    line-height: 20px;
  }
  .contact-list li { display: flex; align-items: center; gap: 8px; }
  .contact-list svg { width: 13px; height: 13px; fill: var(--ink); }
  .address {
    position: absolute; right: 42px; top: 270px;
    font-style: normal; text-align: right;
    font-size: 16px; color: var(--text);
    line-height: 20px;
  }
  .footer-band {
    position: absolute; left: 0; top: 314px;
    width: 640px; height: 52px;
  }
  .website {
    position: absolute; right: 42px; top: 337px;
    font-size: 16px; color: var(--white);
  }

  /* Back side */
  .card-back {
    left: 284px; top: 567px;
    width: 646px; height: 369px;
    background: radial-gradient(ellipse at 50% 45%, var(--green-light) 0%, var(--green) 75%);
    display: flex; align-items: center; justify-content: center;
  }
  .back-brand {
    display: flex; align-items: center; gap: 16px;
    font-weight: 700; font-size: 34px;
    color: var(--ink);
    letter-spacing: 1px;
    text-transform: uppercase;
  }
  .back-brand .brand-square { width: 28px; height: 28px; background: var(--ink); }
</style>
</head>
<body>
<main class="canvas">

  <section class="card card-front" aria-label="Business card front">
    <div class="front-brand"><span class="brand-square"></span><span>Ridgecrest Design + Build</span></div>

    <h1 class="person-name">Jonah Whitfield</h1>
    <p class="person-title">President</p>
    <div class="divider"></div>

    <ul class="contact-list">
      <li>
        <svg viewBox="0 0 24 24" aria-hidden="true"><path d="M6.6 10.8a15.2 15.2 0 0 0 6.6 6.6l2.2-2.2a1 1 0 0 1 1-.25 11.4 11.4 0 0 0 3.6.57 1 1 0 0 1 1 1V20a1 1 0 0 1-1 1A17 17 0 0 1 3 4a1 1 0 0 1 1-1h3.5a1 1 0 0 1 1 1c0 1.25.2 2.45.57 3.6a1 1 0 0 1-.25 1z"/></svg>
        <span>(555) 014-2290</span>
      </li>
      <li>
        <svg viewBox="0 0 24 24" aria-hidden="true"><path d="M2 5h20v14H2z M3.5 6.5 12 13l8.5-6.5" stroke="#f4f4f5" stroke-width="1.6" /></svg>
        <span>hello@ridgecrestbuild.com</span>
      </li>
    </ul>

    <address class="address">214 Alder Court<br>Maple Hollow, NY 10990</address>

    <svg class="footer-band" viewBox="0 0 640 52" aria-hidden="true">
      <defs>
        <linearGradient id="stripeGreen" x1="0" x2="1" y1="0" y2="0">
          <stop offset="0" stop-color="#7fba27"/>
          <stop offset="0.5" stop-color="#b4d97a"/>
          <stop offset="1" stop-color="#7fba27"/>
        </linearGradient>
      </defs>
      <polygon points="0,21 366,21 350,38 0,38" fill="url(#stripeGreen)"/>
      <polygon points="0,39 349,39 372,11 640,11 640,52 0,52" fill="#0b0b0b"/>
    </svg>
    <p class="website">www.ridgecrestbuild.com</p>
  </section>

  <section class="card card-back" aria-label="Business card back">
    <div class="back-brand"><span class="brand-square"></span><span>Ridgecrest Design + Build</span></div>
  </section>

</main>
</body>
</html>
```